Brochure Design Project - Brelwick Motors Auto Repair Centre

We require a high quality brochure (A3 folded to A4) for us to send to local businesses to try and get more sales. We would like to keep our current colour scheme from our flyers. We are garagemark approved so we require this logo to be included in the design. The font used on our flyer is QuickLinesRG available from fontvault-example.com
This is a brief of the information we require on our brochure (the feedback from our current customers still to be received but it will be limited to 1 line each) :
Introduction to Brelwick Motors
Based in Cumbernauld, Brelwick Motors are a family run Auto service centre and believe in giving helpful, friendly expert advice in plain English. We have a wealth of experience in a wide range of vehicles and we invest heavily in equipment to ensure our work is completed to the highest possible quality standards.
It is our aim to deliver a quality service at competitive rates for our customers. We have just expanded by investing in a new 4000 sq/ft workshop to help support our ever expanding customer base.
Why are we the best choice for your business?
Choosing a garage for your business can be a tough decision. Who do you choose and who do you trust? Cost will of course be high on your list, so why take your car to a main dealer and pay main dealer prices?
• Brelwick Motors Cumbernauld can carry out servicing and repairs to main dealer standards without the high prices. We can also maintain your vehicles warranty by using genuine manufacturer's parts.
• Communication is key – we never leave you wondering when your vehicle is going to be returned. 98% of vehicles we maintain are returned the same day.
• We never carry out any work to a vehicle without prior agreement – so no unexpected bills. You always get a fully itemised VAT invoice.
• We can arrange payment terms that are suitable to both businesses.
• We have flexibility with our working hours to ensure your fleet stays on the road no matter how big or small.
• We also pride ourselves on providing a professional and efficient service, your vehicle will be looked after as if it was our own pride and joy.
How can we guarantee quality?
Garage mark is the Trading Standards code of practice for garages. We are the only independent garage in Cumbernauld to achieve this standard. We are audited to ensure we comply with the code at all times and we must follow a strict complaints procedure should the need arise.
All parts fitted are covered by a 3 month or 6000 mile warranty. *Does not include wear and tear
What services can we offer your business?
MOT Testing
Vehicle Servicing
Budget & Performance Tyres
Mechanical Repairs
Exhausts, DPF filters & CAT’s
Brake repair specialist
Same day Clutch repairs
Gearboxes
Starter motors
Alternators
Wheel Alignment
MOT Welding
Replacement Batteries
ECU Fault Diagnostics & Service resets
Collection and drop off services
We are comprehensively insured to drive all of our customers’ vehicles so we can collect vehicles at a time that suits you and deliver them back with minimal impact to your business. The only time we will ever drive your vehicles is during transportation or testing.
Our current business customers – testimonials
Pettigrew Roofing
Crest Fitting
Hollowbys
Ruvan Loader training
Sample price list
£74.17 for car service/small vans
£91.67 for commercials up to 3500kgs (class IV)
Mot’s £35 for cars and vans (class IV)
Tyre sample prices – Ford Focus £36.95, Renault Kangoo £32.45, Ford Transit £41.55.
Labour rate of £35.00ph
All prices exclude VAT at applicable rate, unless stated otherwise and are correct at time of printing. Subject to change without prior notice. No VAT on MOT's
Contact Us
Brelwick Motors can be contacted to discuss your individual requirement by -
Phone: 01236 482915
Email: sales@brelwick-example.co.uk
Mon – Fri 8.00am – 5.30pm
Sat – 8.00am – 4.00pm
Target Market(s)
local businesses
Industry/Entity Type
Garage
Requirements
Must have
- garagemark logo
brelwick motors logo

```html
<!DOCTYPE html>
<html lang="en">
<head>
<meta charset="utf-8">
<title>Brelwick Motors Auto Repair Centre – Business Brochure</title>
<link href="https://fonts.googleapis.com/css2?family=Michroma&display=swap" rel="stylesheet">
<style>
  :root {
    --frame: #2e3234;
    --edge: #f2f2f2;
    --panel-blue: #1ba3f2;
    --accent-cyan: #19b2ef;
    --heading-yellow: #f6ec12;
    --body-ink: #0a0f14;
    --swoosh-dark: #3b3d3f;
  }
  * { box-sizing: border-box; margin: 0; padding: 0; }
  html, body { width: 1200px; height: 854px; overflow: hidden; background: var(--edge); }
  .brochure {
    position: relative; width: 1200px; height: 854px;
    background: var(--edge);
    font-family: "Michroma", sans-serif;
  }
  .spread {
    position: absolute; left: 6px; top: 6px; width: 1188px; height: 842px;
    background: var(--frame);
  }
  .page {
    position: absolute; top: 32px; width: 531px; height: 459px;
    background: var(--panel-blue); overflow: hidden;
  }
  .page--left { left: 37px; }
  .page--right { left: 620px; }
  .page__swoosh { position: absolute; left: 0; top: 0; width: 531px; height: 44px; }
  .column {
    position: absolute; top: 42px; width: 238px;
    color: var(--body-ink); font-size: 7.5px; line-height: 10.4px;
    text-transform: uppercase; text-align: justify;
  }
  .page--left .column--a { left: 15px; }
  .page--left .column--b { left: 275px; width: 241px; top: 48px; }
  .page--right .column--a { left: 20px; width: 236px; top: 46px; }
  .page--right .column--b { left: 279px; width: 236px; top: 46px; }
  .heading {
    color: var(--heading-yellow); font-size: 10.6px; line-height: 15px;
    font-weight: 400; text-transform: uppercase; text-align: left;
    letter-spacing: -0.2px; margin: 0 0 2px;
  }
  .section { margin-bottom: 8px; }
  .bullets { list-style: none; }
  .bullets li { position: relative; padding-left: 16px; margin-top: 10px; }
  .bullets li::before {
    content: ""; position: absolute; left: 2px; top: 4px;
    width: 3px; height: 3px; border-radius: 50%; background: var(--body-ink);
  }
  .bullets--first li:first-child { margin-top: 0; }
  .services { list-style: none; margin-top: 18px; }
  .services li { position: relative; padding-left: 11px; line-height: 10.4px; margin-bottom: 9.4px; text-align: left; }
  .services li::before {
    content: ""; position: absolute; left: 0; top: 4px;
    width: 3px; height: 3px; border-radius: 50%; background: var(--body-ink);
  }
  .clients { list-style: none; margin-top: 14px; }
  .clients li { margin-bottom: 13px; text-align: left; }
  .gap-top { margin-top: 16px; }
  .reception-strip {
    position: absolute; left: 37px; top: 497px; width: 1114px; height: 7px;
    background: var(--accent-cyan);
  }
  .reception-photo {
    position: absolute; left: 37px; top: 504px; width: 1114px; height: 308px;
    background:
      linear-gradient(90deg, rgba(40,44,48,0.55) 0%, rgba(40,44,48,0.1) 16%, rgba(0,0,0,0) 30%, rgba(0,0,0,0) 85%, rgba(40,44,48,0.25) 100%),
      linear-gradient(180deg, #eeede8 0%, #e2e0d8 52%, #b89a74 62%, #8a6444 80%, #5e4430 100%);
  }
</style>
</head>
<body>
<main class="brochure">
  <div class="spread">

    <section class="page page--left">
      <svg class="page__swoosh" viewBox="0 0 531 44" preserveAspectRatio="none" aria-hidden="true">
        <defs>
          <linearGradient id="swooshLeft" x1="0" y1="0" x2="1" y2="0">
            <stop offset="0" stop-color="#f4f4f4"/>
            <stop offset="0.5" stop-color="#cfcfcf"/>
            <stop offset="1" stop-color="#9a9a9a"/>
          </linearGradient>
        </defs>
        <path d="M0 0 H531 V10 C430 2 330 4 240 14 C150 24 70 22 0 10 Z" fill="var(--swoosh-dark)"/>
        <path d="M0 10 C70 22 150 24 240 14 C330 4 430 2 531 10 V18 C430 10 330 14 240 22 C150 32 70 30 0 20 Z" fill="url(#swooshLeft)"/>
      </svg>

      <div class="column column--a">
        <div class="section">
          <h2 class="heading">Introduction to Brelwick Motors</h2>
          <p>Based in Cumbernauld, Brelwick Motors are a family run auto service centre and believe in giving helpful, friendly expert advice in plain English. We have a wealth of experience in a wide range of vehicles and we invest heavily in equipment to ensure our work is completed to the highest possible quality standards.</p>
          <p>It is our aim to deliver a quality service at competitive rates for our customers. We have just expanded by investing in a new 4000 sq/ft workshop to help support our ever expanding customer base.</p>
        </div>
        <div class="section">
          <h2 class="heading">Why are we the best choice for your business?</h2>
          <p>Choosing a garage for your business can be a tough decision. Who do you choose and who do you trust? Cost will of course be high on your list, so why take your car to a main dealer and pay main dealer prices?</p>
          <ul class="bullets">
            <li>Brelwick Motors Cumbernauld can carry out servicing and repairs to main dealer standards without the high prices. We can also maintain your vehicles warranty by using genuine manufacturer's parts.</li>
          </ul>
        </div>
      </div>

      <div class="column column--b">
        <ul class="bullets bullets--first">
          <li>Communication is key – we never leave you wondering when your vehicle is going to be returned. 98% of vehicles we maintain are returned the same day.</li>
          <li>We never carry out any work to a vehicle without prior agreement – so no unexpected bills. You always get a fully itemised VAT invoice.</li>
          <li>We can arrange payment terms that are suitable to both businesses.</li>
          <li>We have flexibility with our working hours to ensure your fleet stays on the road no matter how big or small.</li>
          <li>We also pride ourselves on providing a professional and efficient service, your vehicle will be looked after as if it was our own pride and joy.</li>
        </ul>
        <div class="section" style="margin-top:6px">
          <h2 class="heading">How can we guarantee quality?</h2>
          <p>Garage mark is the trading standards code of practice for garages. We are the only independent garage in Cumbernauld to achieve this standard. We are audited to ensure we comply with the code at all times and we must follow a strict complaints procedure should the need arise.</p>
        </div>
      </div>
    </section>

    <section class="page page--right">
      <svg class="page__swoosh" viewBox="0 0 531 44" preserveAspectRatio="none" aria-hidden="true">
        <defs>
          <linearGradient id="swooshRight" x1="0" y1="0" x2="1" y2="0">
            <stop offset="0" stop-color="#9a9a9a"/>
            <stop offset="0.5" stop-color="#cfcfcf"/>
            <stop offset="1" stop-color="#f4f4f4"/>
          </linearGradient>
        </defs>
        <path d="M0 0 H531 V10 C460 22 380 24 290 14 C200 4 100 2 0 10 Z" fill="var(--swoosh-dark)"/>
        <path d="M0 10 C100 2 200 4 290 14 C380 24 460 22 531 10 V20 C460 30 380 32 290 22 C200 12 100 10 0 18 Z" fill="url(#swooshRight)"/>
      </svg>

      <div class="column column--a">
        <p>All parts fitted are covered by a 3 month or 6000 mile warranty. *Does not include wear and tear</p>
        <h2 class="heading">What services can we offer your business?</h2>
        <ul class="services">
          <li>MOT Testing</li>
          <li>Vehicle Servicing</li>
          <li>Budget &amp; Performance Tyres</li>
          <li>Mechanical Repairs</li>
          <li>Exhausts, DPF Filters &amp; CATs</li>
          <li>Brake Repair Specialist</li>
          <li>Same Day Clutch Repairs</li>
          <li>Gearboxes</li>
          <li>Starter Motors</li>
          <li>Alternators</li>
          <li>Wheel Alignment</li>
          <li>MOT Welding</li>
          <li>Replacement Batteries</li>
          <li>ECU Fault Diagnostics &amp; Service Resets</li>
        </ul>
      </div>

      <div class="column column--b">
        <h2 class="heading">Collection and drop off services</h2>
        <p class="gap-top">We are comprehensively insured to drive all of our customers' vehicles so we can collect vehicles at a time that suits you and deliver them back with minimal impact to your business. The only time we will ever drive your vehicles is during transportation or testing.</p>
        <h2 class="heading gap-top">Our current business customers – testimonials</h2>
        <ul class="clients">
          <li>Pettigrew Roofing</li>
          <li>Crest Fitting</li>
          <li>Hollowbys</li>
          <li>Ruvan Loader Training</li>
        </ul>
      </div>
    </section>

    <div class="reception-strip" aria-hidden="true"></div>
    <div class="reception-photo" role="img" aria-label="Panoramic photograph of the garage reception area with wooden floor, stacked tyres, a white front desk, a glass coffee table and black chairs"></div>
  </div>
</main>
</body>
</html>
```